Web Design Project

This as the foundation http://fenlarkstudio.com/demo_viewer/index.php?theme=vostriquewp

Site needs to have a glossy black background with white text…..Extremely modern with a few flares of pallor 5 style but nothing too off the wall, easily understood.

Here are some other reference sites and likes and dislikes that will help: (Probably overkill but we are looking for a cutting edge New York / LA Style )

http://www.brevinandcrewtx.com

Like- The black background with white font is very eye catching and clean. Love the contrast. Black is a great background for photographs and videos

http://maltegrunow.com

Like- Clean homepage, black and white color scheme works well.

http://orvillekastnerphotography.com

Like- Nice Menu, nice B and W contrast

http://www.qvx.com

Like- Like the Menu. Clean and easy.

http://www.saffelmedia.com

Like- Contrast of white background with black font.

Like- Slide show of stills (but should be able to click images to go to video. We’d also like the name of the project)

Like- Drop down menu allows for customer to find service they need without going through all services.

Like- Tells you work that they do right next to the logo.

Dislike- Too much information on homepage. Too much scrolling.

http://www.tundravoxfilms.com

Like- High Res images on home page

Like - The About Me is on homepage and speaks to potential customer directly. “We create award-winning videos for companies like yours.”

Like- Blog is updated with new projects they do. And short, visual entries

Like- “Work” section stands out from website. The background fades to light grey and white when you click on “work” so that the portfolio stands out more. Makes color look more vivid

Like- Black and white color scheme with grey header

http://www.bureau847.com

Like- High Res images on home page pointing to projects

Like- Photograph as background, changes with different links. So work is always showcased and creates contrast. Information is laid over a barely translucent background, which is laid over the picture.

Like- They have a good Attitude about quality of their product

http://www.quillmarsh.net

Like- First thing you see when open page is a clear big statement about what they do, said in a catchy way. They have a Tagline.

http://plinthworks.com

Like- How work is categorized. Client list has links, which take you to their Client page with all their work grouped together. Nice flow and organization shows client relationships. And nice descriptions of what the job was and how it was executed… Way too wordy at times though

http://www.marisadoneimages.com

Like- The homepage is very clean and accessible. Love the color scheme and how Logo is centered between the links.

Of the four designs we have gotten EVERY SINGLE ONE has been a template STOLEN from another site. We are paying for ORIGINAL design. Not copies and templates. Please ONLY submit original designs

```html
<!DOCTYPE html>
<html lang="en">
<head>
<meta charset="utf-8">
<title>Reedwick Productions</title>
<link href="https://fonts.googleapis.com/css2?family=Lobster&family=Cutive+Mono&family=Carlito:wght@400;700&family=Arimo:wght@700&display=swap" rel="stylesheet">
<style>
  :root {
    --white: #ffffff;
    --hero-bg: #f9f9f9;
    --ink: #0b0b0b;
    --nav-bg: #000000;
    --dark-top: #050505;
    --dark-bottom: #1c1c1c;
    --footer-bg: #141414;
    --text-light: #f2f2f2;
    --text-muted: #cfcfcf;
    --text-dim: #9a9a9a;
    --rule: #5a5a5a;
    --control: #2f3234;
    --control-edge: #55595c;
  }
  * { margin: 0; padding: 0; box-sizing: border-box; }
  html, body { width: 1105px; height: 1200px; overflow: hidden; background: var(--white); }
  .page { position: relative; width: 1105px; height: 1200px; overflow: hidden; background: var(--white); font-family: "Carlito", "Calibri", sans-serif; }

  /* Header */
  .nav-button {
    position: absolute; top: 91px; width: 97px; height: 29px;
    background: var(--nav-bg); color: var(--white);
    font-family: "Arimo", Arial, sans-serif; font-weight: 700; font-size: 11.5px; letter-spacing: -0.2px;
    display: flex; align-items: center; justify-content: center; gap: 6px; text-transform: uppercase;
  }
  .nav-button .caret { width: 0; height: 0; border-left: 3px solid transparent; border-right: 3px solid transparent; border-top: 5px solid var(--white); }
  .brand {
    position: absolute; left: 424px; top: 40px; width: 260px; text-align: center; color: var(--ink);
  }
  .brand-mark { display: block; width: 60px; height: 60px; margin: 0 auto 10px; border: 2px solid var(--ink); border-radius: 50%; }
  .brand-name { font-family: "Carlito", sans-serif; font-size: 13px; letter-spacing: 3px; }

  /* Hero */
  .hero-band { position: absolute; left: 0; top: 246px; width: 1105px; height: 367px; background: var(--hero-bg); }
  .hero-tagline {
    position: absolute; left: 75px; top: 268px; font-family: "Lobster", cursive;
    font-size: 50px; line-height: 61px; color: var(--ink); letter-spacing: -1.5px;
  }
  .showreel-still {
    position: absolute; left: 421px; top: 212px; width: 557px; height: 376px;
    background: linear-gradient(180deg, #d9d9d9 0%, #c9c8c6 55%, #8f7a66 72%, #6b5646 100%);
  }
  .video-control { position: absolute; }
  .play-large { left: 682px; top: 389px; }
  .play-small { left: 452px; top: 536px; }
  .control-bar { left: 551px; top: 534px; }
  .slide-dots { position: absolute; left: 925px; top: 592px; display: flex; gap: 6px; }
  .slide-dots span { width: 13px; height: 13px; border-radius: 50%; background: #1a1a1a; box-shadow: inset 0 -2px 2px #555, 0 1px 1px #888; }

  /* Mission */
  .mission-section {
    position: absolute; left: 0; top: 613px; width: 1105px; height: 434px;
    background: linear-gradient(180deg, var(--dark-top) 0%, var(--dark-bottom) 100%);
  }
  .section-title { font-family: "Cutive Mono", "Courier New", monospace; color: var(--white); font-weight: 400; }
  .mission-title { position: absolute; left: 82px; top: 53px; font-size: 32px; }
  .mission-copy { position: absolute; left: 82px; top: 103px; width: 560px; color: var(--text-light); font-size: 16px; line-height: 20.2px; }
  .mission-copy p + p { margin-top: 20px; }
  .featured { position: absolute; left: 697px; top: 60px; width: 289px; }
  .featured-title { font-size: 21px; text-align: center; padding-bottom: 4px; border-bottom: 1px solid var(--rule); }
  .featured-still {
    margin: 19px 0 0 5px; width: 282px; height: 209px;
    background: linear-gradient(135deg, #9c9c9c 0%, #d4d4d4 45%, #8a8a8a 100%);
  }

  /* Footer */
  .site-footer { position: absolute; left: 0; top: 1047px; width: 1105px; height: 153px; background: var(--footer-bg); }
  .footer-nav { position: absolute; left: 83px; top: 44px; display: flex; font-size: 13px; color: var(--text-light); }
  .footer-nav a { color: inherit; text-decoration: none; }
  .footer-nav .sep { width: 1px; height: 13px; background: #bbbbbb; margin-top: 3px; }
  .social-links { position: absolute; left: 884px; top: 42px; display: flex; gap: 10px; }
  .social-links span { width: 24px; height: 24px; border-radius: 50%; background: linear-gradient(180deg, #8a8a8a, #4c4c4c); border: 1px solid #2a2a2a; }
  .contact-line { position: absolute; right: 126px; top: 84px; color: var(--text-light); font-size: 14px; }
  .contact-line strong { font-size: 19px; font-weight: 700; margin-left: 4px; color: var(--white); }
  .address-line { position: absolute; right: 126px; top: 113px; color: var(--text-light); font-size: 14px; }
  .copyright { position: absolute; left: 81px; top: 115px; color: var(--text-dim); font-size: 12px; }
  .copyright b { font-weight: 700; }
</style>
</head>
<body>
<div class="page">
  <header>
    <div class="nav-button" style="left:81px">Services<span class="caret"></span></div>
    <div class="nav-button" style="left:193px">Gallery<span class="caret"></span></div>
    <div class="nav-button" style="left:303px">About us</div>
    <div class="brand">
      <span class="brand-mark"></span>
      <span class="brand-name">Reedwick Productions</span>
    </div>
    <div class="nav-button" style="left:659px">Show reel<span class="caret"></span></div>
    <div class="nav-button" style="left:771px">Clients</div>
    <div class="nav-button" style="left:881px">Contact</div>
  </header>

  <section class="hero">
    <div class="hero-band"></div>
    <h1 class="hero-tagline">Video Production<br>Creative Services<br>Digital media</h1>
    <div class="showreel-still" role="img" aria-label="Show reel still: a dancer in white stretching backwards on a wooden studio floor"></div>
    <svg class="video-control play-large" width="40" height="40" viewBox="0 0 40 40">
      <rect x="1" y="1" width="38" height="38" rx="3" fill="var(--control)" stroke="var(--control-edge)"/>
      <path d="M15 11 L28 20 L15 29 Z" fill="#fff"/>
    </svg>
    <svg class="video-control play-small" width="58" height="38" viewBox="0 0 58 38">
      <rect x="1" y="1" width="56" height="36" rx="3" fill="var(--control)" stroke="var(--control-edge)"/>
      <path d="M23 10 L37 19 L23 28 Z" fill="#fff"/>
    </svg>
    <svg class="video-control control-bar" width="368" height="40" viewBox="0 0 368 40">
      <rect x="1" y="1" width="366" height="38" rx="3" fill="var(--control)" stroke="var(--control-edge)"/>
      <text x="12" y="25" fill="#fff" font-family="Carlito, sans-serif" font-size="14">00:00</text>
      <rect x="58" y="14" width="201" height="11" fill="#2b2d2f" stroke="#cfcfcf" stroke-width="1.5"/>
      <g fill="#fff">
        <rect x="270" y="13" width="3" height="13"/><rect x="276" y="13" width="3" height="13"/>
        <rect x="282" y="13" width="3" height="13"/><rect x="288" y="13" width="3" height="13"/>
        <rect x="294" y="13" width="3" height="13"/><rect x="300" y="13" width="3" height="13"/>
        <rect x="306" y="13" width="3" height="13"/><rect x="312" y="13" width="3" height="13"/>
        <rect x="318" y="13" width="3" height="13" fill="#888"/>
      </g>
      <g stroke="#fff" stroke-width="2" fill="none">
        <path d="M338 14 L346 22 M346 14 L338 22"/>
        <path d="M337 17 V13 H341 M343 13 H347 V17 M347 19 V23 H343 M341 23 H337 V19"/>
      </g>
    </svg>
    <div class="slide-dots"><span></span><span></span><span></span></div>
  </section>

  <section class="mission-section">
    <h2 class="section-title mission-title">Our mission</h2>
    <div class="mission-copy">
      <p>Lorem ipsum dolor sit amet, consectetur adipiscing elit. Proin massa lorem, adipiscing ornare elementum non, rutrum et ante. Phasellus adipiscing, justo sit amet fermentum molestie, metus arcu ornare velit, vitae mollis libero elit et orci. Quisque sed bibendum turpis. Proin id nibh ultrices, tincidunt risus vitae, imperdiet justo. Sed quis dui commodo sapien pulvinar pretium. Nulla mollis ac diam et aliquet. Donec elementum elit a justo laoreet bibendum.</p>
      <p>Duis tempor rhoncus dolor, at mattis nulla tincidunt a. Fusce ultricies ligula vitae aliquam commodo. Aenean est ante, mollis a erat ac, aliquet tincidunt est. Suspendisse porta mattis diam imperdiet auctor.</p>
    </div>
    <aside class="featured">
      <h3 class="section-title featured-title">Featured Projects</h3>
      <div class="featured-still" role="img" aria-label="Black and white photo of a film clapperboard lying on concrete"></div>
    </aside>
  </section>

  <footer class="site-footer">
    <nav class="footer-nav">
      <a style="width:63px">Services</a><span class="sep"></span>
      <a style="margin-left:37px;width:71px">Gallery</a><span class="sep"></span>
      <a style="margin-left:32px;width:77px">About us</a><span class="sep"></span>
      <a style="margin-left:30px;width:71px">Show reel</a><span class="sep"></span>
      <a style="margin-left:31px;width:55px">Clients</a><span class="sep"></span>
      <a style="margin-left:23px">Contact</a>
    </nav>
    <div class="social-links" aria-label="Social links"><span></span><span></span><span></span></div>
    <p class="contact-line">Contact Us <strong>123.456.789</strong></p>
    <p class="address-line">Street Main 12 - City- State- Zip Code 12345</p>
    <p class="copyright"><b>Reedwick</b> · 2013 © All rights reserved</p>
  </footer>
</div>
</body>
</html>
```